New travel store signage for Kelvane Journeys to attract luxury travellers.

Hello,
We are looking to change the signage of our stores. The signage must include the following:
1. Kelvane Journeys Logo (attached)
2. The text...The Travel & Cruise Experts
3. Brand Colours ( Fb0196, 412266, d41d84 and ffffff)
Please note the signage design must be central and only cover two thirds of the store front. We have also attached an image of one of our new stores which might be helpful when preparing a mock up.

We are looking for a quick turnaround on this, making a decision within 48 hours.

Target Market(s)

Retail

Industry/Entity Type

Travel Agency

Font styles to use
Other font styles liked:
• Radley

Colors
E54698
E96AAD
F1A4CE
F9D9EA
FCEFF6
6B429C
8869AF
B7A5CE
E3DAEB
F3F0F8

Requirements
Must have
• Hello, We are looking to change the signage of our stores. The signage must include the following: 1. Kelvane Journeys Logo (attached) 2. The text...The Travel & Cruise Experts 3. Brand Colours ( Fb0196, 412266, d41d84 and ffffff) Please note the signage design must be central and only cover two thirds of the store front.
Should not have
• different colour or fonts. Gradient design.

```html
<!DOCTYPE html>
<html lang="en">
<head>
<meta charset="UTF-8">
<title>Kelvane Journeys – Store Fascia Sign</title>
<link rel="stylesheet" href="https://fonts.googleapis.com/css2?family=Radley&display=swap">
<style>
  :root {
    --backdrop: #dadada;
    --white: #ffffff;
    --brand-pink: #d41d84;
    --brand-magenta: #fb0196;
    --brand-purple: #412266;
    --deep-purple: #34184f;
  }
  * { margin: 0; padding: 0; box-sizing: border-box; }
  html, body {
    width: 1200px;
    height: 919px;
    overflow: hidden;
    background: var(--backdrop);
  }
  .canvas {
    position: relative;
    width: 1200px;
    height: 919px;
  }
  .fascia-sign {
    position: absolute;
    left: 60px;
    top: 392px;
    width: 1080px;
    height: 134px;
    background: var(--white);
    overflow: hidden;
  }
  .fascia-band {
    position: absolute;
    inset: 0;
    width: 1080px;
    height: 134px;
  }
  .brand-lockup {
    position: absolute;
    left: 0;
    top: 0;
    width: 306px;
    height: 134px;
    display: flex;
    align-items: center;
    justify-content: center;
    gap: 12px;
  }
  .brand-dot {
    width: 22px;
    height: 22px;
    border-radius: 50%;
    background: var(--brand-pink);
    flex: none;
  }
  .brand-name {
    font-family: "Radley", Georgia, serif;
    font-size: 27px;
    font-weight: 400;
    color: var(--brand-purple);
    white-space: nowrap;
  }
  .tagline {
    position: absolute;
    left: 372px;
    top: 0;
    width: 620px;
    height: 134px;
    display: flex;
    align-items: center;
    font-family: "Radley", Georgia, serif;
    font-size: 51px;
    font-weight: 400;
    color: var(--white);
    white-space: nowrap;
    letter-spacing: -0.3px;
  }
</style>
</head>
<body>
  <main class="canvas">
    <section class="fascia-sign" aria-label="Kelvane Journeys store fascia">
      <svg class="fascia-band" viewBox="0 0 1080 134" aria-hidden="true">
        <defs>
          <linearGradient id="bandGradient" x1="0" y1="0" x2="1" y2="0">
            <stop offset="0" stop-color="var(--brand-pink)"/>
            <stop offset="0.3" stop-color="var(--brand-pink)"/>
            <stop offset="0.62" stop-color="#7e1a6e"/>
            <stop offset="0.85" stop-color="var(--brand-purple)"/>
            <stop offset="1" stop-color="var(--deep-purple)"/>
          </linearGradient>
        </defs>
        <polygon class="chevron-band" points="337,0 1080,0 1080,134 337,134 306,67" fill="url(#bandGradient)"/>
        <polygon class="chevron-shade" points="540,0 1080,0 1080,134 540,134 520,67" fill="#000" opacity="0.04"/>
        <polygon class="chevron-shade" points="760,0 1080,0 1080,134 760,134 740,67" fill="#000" opacity="0.05"/>
      </svg>
      <div class="brand-lockup">
        <span class="brand-dot"></span>
        <span class="brand-name">Kelvane Journeys</span>
      </div>
      <p class="tagline">The Travel &amp; Cruise Experts</p>
    </section>
  </main>
</body>
</html>
```